Business Card - Self Employed Director

My husband needs a business card design. 2 sided printing required.

He is self employed, in the vineyard management and renewable energy sectors (see below for more information) and design and accent colors should reflect this.

Design should be modern but classic and professional too.

Card to show personal contact information only. Exact information subject to confirmation on finalizing design as we are moving soon and need to confirm the exact details.

Dorian Fellowes
email: dorian.fellowes@quillbarrow.example
mobile: 021 048 53117
home: +64 (0) 3 6142 875
184 Corbin Ridge Rise, RD4 Fenwold, Harrowdale, NZ 7384

I like the attached design by Pik for inspiration.

The reverse side should show name in bottom right corner with the pattern possibly reflecting renewable energy? Waves? Wind? Sea green, teal? Fresh, clean
Image on reverse should not be a photograph but a clean graphic based print on white background. Sans serfic fonts, Charcoal grey not black with accent colors reflected on the back?

Print ready artwork will be required. Please ask any questions :-) THANKS

Printing

Font styles to use
Sans Serif

Colors
86cfc6
ffffff
85abd2

Requirements
Must have
• Contact information as show
Should not have
• Anything cute, no red. No fancy flourish fonts.

```html
<!DOCTYPE html>
<html lang="en">
<head>
<meta charset="utf-8">
<title>Dorian Fellowes — Business Card</title>
<link rel="stylesheet" href="https://fonts.googleapis.com/css2?family=Roboto:wght@300;400&display=swap">
<style>
  :root {
    --backdrop: #6c6d71;
    --card: #ffffff;
    --charcoal: #4a4b4d;
    --charcoal-soft: #5f6062;
    --sea-green: #86cfc6;
    --sky-blue: #85abd2;
    --rule: #85abd2;
  }
  html, body {
    margin: 0;
    padding: 0;
    overflow: hidden;
  }
  body {
    width: 1200px;
    height: 900px;
    background: var(--backdrop);
    position: relative;
    font-family: "Roboto", Arial, sans-serif;
    color: var(--charcoal);
  }
  .card {
    position: absolute;
    left: 291px;
    width: 616px;
    height: 343px;
    background: var(--card);
    overflow: hidden;
  }
  .card--front { top: 87px; }
  .card--back { top: 467px; }

  .pattern-band {
    position: absolute;
    display: block;
  }
  .card--front .pattern-band {
    left: 77px;
    top: 0;
    width: 214px;
    height: 343px;
  }
  .card--back .pattern-band {
    left: 0;
    top: 0;
    width: 616px;
    height: 343px;
  }

  .name {
    position: absolute;
    margin: 0;
    font-weight: 300;
    font-size: 22px;
    line-height: 20px;
    letter-spacing: -0.3px;
    color: var(--charcoal);
  }
  .name span { display: block; }
  .name__rule {
    position: absolute;
    height: 1px;
    background: var(--rule);
  }
  .card--front .name { left: 307px; top: 150px; }
  .card--front .name__rule { left: 304px; top: 190px; width: 97px; }
  .card--back .name { left: 505px; top: 278px; }
  .card--back .name__rule { left: 502px; top: 318px; width: 92px; }

  .contact {
    position: absolute;
    left: 307px;
    margin: 0;
    font-weight: 300;
    font-size: 11.5px;
    line-height: 16px;
    color: var(--charcoal-soft);
    font-style: normal;
  }
  .contact--mobile { top: 197px; }
  .contact--details { top: 274px; }
</style>
</head>
<body>

  <section class="card card--front" aria-label="Card front">
    <svg class="pattern-band" viewBox="0 0 214 343" role="img" aria-label="Striped interlacing band pattern in sea green and sky blue">
      <defs>
        <linearGradient id="band-front" x1="0" y1="0" x2="0" y2="1">
          <stop offset="0" stop-color="#86cfc6" stop-opacity="0.55"/>
          <stop offset="0.5" stop-color="#86cfc6" stop-opacity="0.45"/>
          <stop offset="0.5" stop-color="#85abd2" stop-opacity="0.45"/>
          <stop offset="1" stop-color="#85abd2" stop-opacity="0.6"/>
        </linearGradient>
      </defs>
      <rect width="214" height="343" fill="url(#band-front)"/>
    </svg>

    <h1 class="name"><span>Dorian</span><span>Fellowes</span></h1>
    <div class="name__rule"></div>

    <p class="contact contact--mobile">Mobile: 021 048 53117</p>

    <address class="contact contact--details">
      Home: +64 (0) 3 6142 875<br>
      email: dorian.fellowes@quillbarrow.example<br>
      184 Corbin Ridge Rise, RD4 Fenwold,<br>
      Harrowdale, NZ 7384
    </address>
  </section>

  <section class="card card--back" aria-label="Card back">
    <svg class="pattern-band" viewBox="0 0 616 343" role="img" aria-label="Repeating striped interlacing band pattern in sea green and sky blue">
      <defs>
        <linearGradient id="band-back" x1="0" y1="0" x2="0" y2="1">
          <stop offset="0" stop-color="#86cfc6" stop-opacity="0.5"/>
          <stop offset="0.5" stop-color="#86cfc6" stop-opacity="0.4"/>
          <stop offset="0.5" stop-color="#85abd2" stop-opacity="0.4"/>
          <stop offset="1" stop-color="#85abd2" stop-opacity="0.55"/>
        </linearGradient>
      </defs>
      <rect width="616" height="343" fill="url(#band-back)"/>
    </svg>

    <h2 class="name"><span>Dorian</span><span>Fellowes</span></h2>
    <div class="name__rule"></div>
  </section>

</body>
</html>
```